Exterior cleaning company requires a eye catching a5 leaflet

we need some updated leaflet designs, a5 folded, we are targeting all exterior cleaning contracts, including roof cleaning & treatment, render cleaning & Treatment, driveways, block paving cleaning using the latest in low pressure cleaning technologies along side high pressure jetwashing. gutter clearance and flushing, water fed telescopic pole window cleaning of difficult to reach windows and high buildings. our website : www.tkbellowsec.co.uk facebook page: https://www.facebook.com/tkbellowsexteriorcareltd Instagram: https://www.instagram.com/tkbellowsec/ a quick google search of roof cleaning, soft washing etc will provide results of what we are doing

Target Market(s)

home owners, commercial clients

Font styles to use
Serif
Sans Serif

Requirements
Must have
• A5 Landscape folded leaflet, front page with company information and bullet points of main works : window & conservatory cleaning, roof cleaning & treatment, Render cleaning & treatment, pressure washing, soft washing, gutter clearing, pressure washing of patios, driveways, gutters, fascias (more info can be provided on techniques etc if required)

```html
<!DOCTYPE html>
<html lang="en">
<head>
<meta charset="utf-8">
<title>TK Bellows Exterior Care – A5 Leaflet</title>
<link href="https://fonts.googleapis.com/css2?family=Montserrat:wght@400;500;700;800&family=Roboto+Condensed:wght@400;700&display=swap" rel="stylesheet">
<style>
:root{
  --stage:#b7b7b7;
  --ink-dark:#2f2f2f;
  --ink-band:#262626;
  --mid-grey:#9b9b9b;
  --icon-grey:#555555;
  --paper:#ffffff;
  --paper-soft:#f1f1f1;
  --text:#1e1e1e;
  --text-soft:#555555;
}
*{margin:0;padding:0;box-sizing:border-box}
html,body{width:931px;height:1200px;overflow:hidden;background:var(--stage)}
body{font-family:"Montserrat",sans-serif;color:var(--text)}
.canvas{position:relative;width:931px;height:1200px;overflow:hidden}
.spread{position:absolute;left:83px;width:750px;height:529px;background:var(--paper);box-shadow:0 2px 6px rgba(0,0,0,.25);overflow:hidden}
.spread--outside{top:52px}
.spread--inside{top:618px}
.panel{position:absolute;top:0;height:100%;width:375px}
.panel--left{left:0}
.panel--right{left:375px;background:linear-gradient(135deg,#f6f6f6,#ececec)}
.abs{position:absolute}

/* about */
.about{left:0;top:0;width:375px;height:403px;background:var(--ink-dark);color:#fff}
.section-title{position:absolute;left:0;width:100%;text-align:center;font-size:15px;font-weight:400;letter-spacing:.2px}
.section-title b{font-weight:800}
.section-rule{position:absolute;width:34px;height:1px;left:50%;margin-left:-17px;background:currentColor;opacity:.6}
.about-copy{position:absolute;left:30px;width:311px;top:78px;font-size:7.4px;line-height:9.1px;text-align:justify;text-align-last:center}
.about-copy p{margin-bottom:18px}

/* contact */
.contact-tab{left:0;top:390px;width:142px;height:27px;background:var(--mid-grey);clip-path:polygon(0 0,100% 0,94% 100%,0 100%);color:#fff;font-weight:700;font-size:14px;line-height:27px;padding-left:21px;white-space:nowrap}
.contact-slash{left:135px;top:390px;width:12px;height:27px;background:var(--paper);clip-path:polygon(75% 0,100% 0,35% 100%,10% 100%)}
.contact-list{left:21px;top:427px;font-size:9.6px;line-height:13px;list-style:none;white-space:nowrap}
.contact-list li{display:flex;align-items:center;gap:4px}
.contact-list svg{width:8px;height:8px}
.bank{left:33px;top:473px;font-size:7.8px;line-height:10px;white-space:nowrap}
.bank b{font-weight:700}
.map{left:231px;top:387px;width:120px;height:120px;border-radius:50%;border:5px solid #8e8e8e;background:radial-gradient(circle at 55% 50%,#f2f2f0,#e2e4e2)}
.band-foot{height:17px;background:var(--mid-grey);color:#fff;font-size:7.6px;letter-spacing:2px;line-height:17px;font-weight:500;white-space:nowrap}
.band-foot--right{right:0;width:205px;clip-path:polygon(8% 0,100% 0,100% 100%,0 100%);padding-left:26px}
.band-foot--left{left:0;width:195px;clip-path:polygon(0 0,91% 0,100% 100%,0 100%);padding-left:20px}
.base-strip{left:0;right:0;bottom:0;height:15px;background:linear-gradient(#dcdcdc,#f3f3f3)}

/* brand */
.brand-mark{border-radius:50%;border:1px solid #333;background:var(--paper)}
.brand-name{font-family:"Roboto Condensed",sans-serif;font-weight:700;font-size:26px;line-height:28px;color:var(--text);white-space:nowrap}
.brand-sub{font-family:"Roboto Condensed",sans-serif;font-size:12.5px;line-height:15px;color:var(--text);white-space:nowrap}
.brand-tel{font-family:"Roboto Condensed",sans-serif;font-size:15px;line-height:19px;color:var(--text);white-space:nowrap}

/* hero */
.hero-bar{left:0;top:117px;width:192px;height:8px;background:var(--ink-band);clip-path:polygon(0 0,100% 0,97% 100%,0 100%)}
.hero-photo{left:0;top:125px;width:375px;height:278px;background:linear-gradient(100deg,#4b5140 0%,#3c4236 35%,#2d3133 60%,#474b4e 100%)}
.hero-title{left:0;width:375px;top:214px;text-align:center;color:#fff;font-weight:500;font-size:28px;line-height:33px;letter-spacing:.3px}
.hero-sub{left:0;width:375px;top:281px;text-align:center;color:#fff;font-size:8.6px;font-weight:500}
.works-band{left:0;top:403px;width:375px;height:27px;background:var(--ink-band);color:#fff;text-align:center;font-weight:700;font-size:15px;line-height:27px}
.works-list{list-style:none;font-size:8.9px;line-height:10.7px;color:var(--text);white-space:nowrap}
.works-list li{display:flex;align-items:center;gap:6px}
.works-list svg{width:7px;height:7px;flex:none}

/* services */
.services{left:0;top:0;width:375px;height:303px;background:var(--ink-dark);color:#fff}
.svc{position:absolute;width:120px}
.svc h3{font-size:6.2px;font-weight:700;line-height:7px}
.svc p{font-size:4.7px;line-height:6px}
.svc--l{left:15px;text-align:right}
.svc--r{left:243px;text-align:left}
.svc-icon{position:absolute;width:40px;height:40px;border-radius:50%;background:var(--icon-grey)}
.svc-icon svg{width:40px;height:40px}

/* photo strip */
.strip-photo{top:303px;height:99px;width:375px}
.strip-photo--a{left:0;background:linear-gradient(90deg,#4a3b33,#6a5a4f 55%,#c9cbcc 80%,#8b8f92)}
.strip-photo--b{left:375px;background:linear-gradient(90deg,#3f3c36,#5f4a40 40%,#6f5448 70%,#4a3c36)}
.strip-word{width:375px;text-align:center;top:343px;color:#fff;font-size:15px;letter-spacing:.6px}

.cta{left:0;width:375px;text-align:center;white-space:nowrap}
.cta-head{top:421px;font-weight:800;font-size:20px}
.cta-call{top:444px;font-weight:500;font-size:17px;color:#444}
.cta-ask{top:468px;font-size:9px;color:#222}

/* areas */
.area{position:absolute;width:80px;margin-left:-40px;text-align:center;font-size:7.6px;color:#333;white-space:nowrap}
.area svg{display:block;margin:0 auto 5px;width:12px;height:17px}
</style>
</head>
<body>
<div class="canvas">

  <!-- ========== OUTSIDE SPREAD ========== -->
  <section class="spread spread--outside">
    <div class="panel panel--left">
      <div class="abs about">
        <h2 class="section-title" style="top:42px">ABOUT <b>TK BELLOWS</b></h2>
        <span class="section-rule" style="top:57px"></span>
        <div class="about-copy">
          <p>TK Bellows Exterior Care is Southport’s most reliable, professional cleaning company who have been providing cleaning services across the North West for 10 years!</p>
          <p>At TK Bellows, our mission is to lead our sector in providing all of our customers with an outstanding cleaning service that keeps ourselves one step ahead of our competition. All of our staff are uniformed, polite, courteous and always happy to help. We aim to build long lasting relationships with our customers, and offer a 5* customer service team to help resolve any issues that may arise.</p>
          <p>Whether it’s to improve overall results or safety, we are always on the lookout for the latest equipment that gives the best finish possible. At TK Bellows our staff use the reach &amp; wash system, otherwise known as the ‘water fed pole’. A technique which compared to traditional window cleaning, reaches your windows and frames safely from the ground, even in hard to reach areas such as above conservatories or dormer windows. This prevents any damage to your property from equipment and prevents accidents.</p>
          <p>We like to keep things simple so our visits to you run as smoothly as possible. Understanding that all of our customers aren’t always at home when we call, we have a call ahead / messaging service to let you know that we are due that day so gates / garage doors may be left unlocked should you wish we didn’t have to climb over. We also provide a secure, key holding service if you’d prefer us to be able to lock up after we’ve finished.</p>
          <p>Our window cleaning round varies from domestic houses to commercial buildings, shops, schools, factories, blocks of flats and much more. Please refer to the ‘services’ page of our website for further information on other aspects of our cleaning.</p>
        </div>
      </div>

      <div class="abs contact-tab">CONTACT US</div>
      <div class="abs contact-slash"></div>

      <ul class="abs contact-list">
        <li><svg viewBox="0 0 10 10"><circle cx="5" cy="5" r="4.4" fill="none" stroke="#333" stroke-width=".8"/><path d="M3.4 2.8l1 1-.5.6c.3.7.8 1.2 1.5 1.5l.6-.5 1 1-.7.8C4.8 7 3 5.2 2.8 3.5z" fill="#333"/></svg>01632 960 481</li>
        <li><svg viewBox="0 0 10 10"><circle cx="5" cy="5" r="4.4" fill="none" stroke="#333" stroke-width=".8"/><rect x="2.8" y="3.4" width="4.4" height="3.2" fill="none" stroke="#333" stroke-width=".7"/><path d="M2.8 3.4L5 5.2l2.2-1.8" fill="none" stroke="#333" stroke-width=".7"/></svg>info@tkbellowsec.co.uk</li>
        <li><svg viewBox="0 0 10 10"><circle cx="5" cy="5" r="4.4" fill="none" stroke="#333" stroke-width=".8"/><circle cx="5" cy="4.4" r="1.3" fill="none" stroke="#333" stroke-width=".7"/><path d="M5 7.6L3.6 5.3M5 7.6l1.4-2.3" stroke="#333" stroke-width=".7"/></svg>14 marsh lane, northwold, nw4 2qt</li>
      </ul>
      <div class="abs bank"><b>BANK TRANSFER:</b><br>ACCOUNT NUMBER: 12345678<br>SORT CODE: 00-00-00</div>

      <div class="abs map" role="img" aria-label="Street map showing the company location"></div>
      <div class="abs base-strip"></div>
    </div>

    <div class="panel panel--right">
      <div class="abs brand-mark" style="left:68px;top:16px;width:86px;height:86px"></div>
      <div class="abs" style="left:171px;top:28px">
        <div class="brand-name">TK Bellows</div>
        <div class="brand-sub">Exterior Care Ltd</div>
        <div class="brand-tel">Tel: 01632 960 481</div>
      </div>

      <div class="abs hero-bar"></div>
      <div class="abs hero-photo" role="img" aria-label="Photo of a cleaner using a water fed pole on a large glass building beside a patio"></div>
      <h1 class="abs hero-title">TK BELLOWS<br>EXTERIOR CARE</h1>
      <div class="abs hero-sub">Commercial · Domestic · Industrial · Retail Cleaning</div>

      <div class="abs works-band">OUR MAIN WORKS</div>
      <ul class="abs works-list" style="left:22px;top:442px">
        <li><svg viewBox="0 0 8 8"><circle cx="4" cy="4" r="3.5" fill="none" stroke="#999" stroke-width=".7"/><path d="M2.3 4l1.2 1.2L6 2.6" fill="none" stroke="#999" stroke-width=".8"/></svg>Window &amp; conservatory cleaning</li>
        <li><svg viewBox="0 0 8 8"><circle cx="4" cy="4" r="3.5" fill="none" stroke="#999" stroke-width=".7"/><path d="M2.3 4l1.2 1.2L6 2.6" fill="none" stroke="#999" stroke-width=".8"/></svg>Roof cleaning &amp; treatment</li>
        <li><svg viewBox="0 0 8 8"><circle cx="4" cy="4" r="3.5" fill="none" stroke="#999" stroke-width=".7"/><path d="M2.3 4l1.2 1.2L6 2.6" fill="none" stroke="#999" stroke-width=".8"/></svg>Render cleaning &amp; treatment</li>
        <li><svg viewBox="0 0 8 8"><circle cx="4" cy="4" r="3.5" fill="none" stroke="#999" stroke-width=".7"/><path d="M2.3 4l1.2 1.2L6 2.6" fill="none" stroke="#999" stroke-width=".8"/></svg>Pressure washing</li>
      </ul>
      <ul class="abs works-list" style="left:220px;top:442px">
        <li><svg viewBox="0 0 8 8"><circle cx="4" cy="4" r="3.5" fill="none" stroke="#999" stroke-width=".7"/><path d="M2.3 4l1.2 1.2L6 2.6" fill="none" stroke="#999" stroke-width=".8"/></svg>Soft Washing</li>
        <li><svg viewBox="0 0 8 8"><circle cx="4" cy="4" r="3.5" fill="none" stroke="#999" stroke-width=".7"/><path d="M2.3 4l1.2 1.2L6 2.6" fill="none" stroke="#999" stroke-width=".8"/></svg>Gutter Clearing</li>
        <li><svg viewBox="0 0 8 8"><circle cx="4" cy="4" r="3.5" fill="none" stroke="#999" stroke-width=".7"/><path d="M2.3 4l1.2 1.2L6 2.6" fill="none" stroke="#999" stroke-width=".8"/></svg>Pressure washing of patios</li>
        <li><svg viewBox="0 0 8 8"><circle cx="4" cy="4" r="3.5" fill="none" stroke="#999" stroke-width=".7"/><path d="M2.3 4l1.2 1.2L6 2.6" fill="none" stroke="#999" stroke-width=".8"/></svg>Driveways, gutters, fascias</li>
      </ul>

      <div class="abs band-foot band-foot--right" style="top:497px">WWW.TKBELLOWSEC.CO.UK</div>
      <div class="abs base-strip"></div>
    </div>
  </section>

  <!-- ========== INSIDE SPREAD ========== -->
  <section class="spread spread--inside">
    <div class="panel panel--left">
      <div class="abs services">
        <h2 class="section-title" style="top:23px">OUR <b>SERVICES</b></h2>
        <span class="section-rule" style="top:48px"></span>

        <div class="svc svc--l" style="top:69px"><h3>EXTERNAL WINDOWS</h3><p>Our staff use the reach &amp; washes system otherwise known as the ‘water fed pole’. A technique which compared to traditional window cleaning, enabling us to reach your windows and frames safely from the ground.</p></div>
        <div class="svc svc--r" style="top:69px"><h3>FASCIAS &amp; GUTTERS</h3><p>Using our telescopic pressure washing lance, we can clean all of your UPVC fascia’s, gutters and drain pipes safely from the ground. The end result your fascia’s and gutters looking like brand new again.</p></div>
        <div class="svc svc--l" style="top:129px"><h3>INTERNAL WINDOWS</h3><p>We clean internal windows and mirrors using the dragon fly system. This method also using purified water can reach them hard to access windows again safely from the ground.</p></div>
        <div class="svc svc--r" style="top:129px"><h3>DRIVEWAYS &amp; PATIOS</h3><p>From small patio areas to large driveways we clean it all. TK Bellows specialise in all driveway and patio cleaning from Indian stone, tarmac, concrete flags to block paving.</p></div>
        <div class="svc svc--l" style="top:184px"><h3>CONSERVATORY ROOFS</h3><p>Has your conservatory roof started to turn green, full of bird muck or dirt? Our water pole method 99% of the time gets rid of all the dirt and grime build up that’s left on your roof.</p></div>
        <div class="svc svc--r" style="top:184px"><h3>GUTTER CLEANING</h3><p>Your property’s gutters and downpipes accumulate all sorts of debris brought by the wind. Using our high reach vac we can clean the gutters safely from the ground eliminating any falls from height.</p></div>
        <div class="svc svc--l" style="top:244px"><h3>SOLAR PANELS</h3><p>Using our access equipment we can clean your solar panels. Anything that blocks the light transmission to your solar PV (or thermal) panels has the potential to lower the performance.</p></div>
        <div class="svc svc--r" style="top:244px"><h3>PRESSURE WASHING</h3><p>We offer a wide range of pressure washing services from garden furniture to house roofs at competitive prices. Cleaning and restoration of all hard surfaces in both the domestic and commercial market.</p></div>

        <div class="svc-icon" style="left:141px;top:65px"><svg viewBox="0 0 40 40" fill="none" stroke="#fff" stroke-width="1.2"><rect x="12" y="11" width="16" height="18"/><rect x="14" y="13" width="12" height="14"/><path d="M20 13v14M14 20h12"/></svg></div>
        <div class="svc-icon" style="left:191px;top:65px"><svg viewBox="0 0 40 40" fill="none" stroke="#fff" stroke-width="1.2"><path d="M11 17v11h12l3-4M25 15h5l-3 10"/><path d="M19 11c-1.5 2-2 3-2 4a2 2 0 004 0c0-1-.5-2-2-4z"/></svg></div>
        <div class="svc-icon" style="left:141px;top:125px"><svg viewBox="0 0 40 40" fill="none" stroke="#fff" stroke-width="1.2"><rect x="11" y="12" width="18" height="16"/><path d="M11 12l5 3v10l-5 3M29 12l-5 3v10l5 3M16 15h8M16 25h8"/></svg></div>
        <div class="svc-icon" style="left:191px;top:125px"><svg viewBox="0 0 40 40" fill="none" stroke="#fff" stroke-width="1.2"><path d="M10 19l10-7 10 7M10 19h20M12 19v10M28 19v10M16 22h8M17 22v7M23 22v7M14 25v4M26 25v4"/></svg></div>
        <div class="svc-icon" style="left:141px;top:180px"><svg viewBox="0 0 40 40" fill="none" stroke="#fff" stroke-width="1.6"><path d="M10 24l10-8 10 8"/></svg></div>
        <div class="svc-icon" style="left:191px;top:180px"><svg viewBox="0 0 40 40" fill="none" stroke="#fff" stroke-width="1.2"><path d="M11 11h18v4H11zM24 15v6h-3v4M15 17v2M18 17v2M15 22v2"/><path d="M15 26c-1 1.5-1.5 2.3-1.5 3a1.5 1.5 0 003 0c0-.7-.5-1.5-1.5-3z"/><path d="M24 25h5l-1 4h-4"/></svg></div>
        <div class="svc-icon" style="left:141px;top:240px"><svg viewBox="0 0 40 40" fill="none" stroke="#fff" stroke-width="1.1"><circle cx="15" cy="14" r="2.5"/><path d="M15 9v1.5M10 14h1.5M11.5 10.5l1 1M18.5 10.5l-1 1"/><path d="M14 19h16l-2 9H12zM13 23.5h16M19 19l-1 9M24 19l-0.5 9M19 28v3M23 28v3"/></svg></div>
        <div class="svc-icon" style="left:191px;top:240px"><svg viewBox="0 0 40 40" fill="none" stroke="#fff" stroke-width="1.1"><rect x="20" y="17" width="8" height="11" rx="1"/><path d="M22 17v-3h4v3M22 21h4M22 24h4M20 30h8M15 12v10a3 3 0 003 3h2M13 10h4M14 12v-2"/></svg></div>
      </div>

      <div class="abs strip-photo strip-photo--a" role="img" aria-label="Photo of a cleaner at a brick period house with the company van parked outside"></div>
      <div class="abs strip-word" style="left:0">PROFESSIONAL</div>

      <div class="abs cta cta-head">OVER 10 YEARS EXPERIENCE</div>
      <div class="abs cta cta-call">CALL US 01632 960481</div>
      <div class="abs cta cta-ask">DO YOU LIKE WHAT YOU SEE?</div>

      <div class="abs band-foot band-foot--left" style="top:496px">WWW.TKBELLOWSEC.CO.UK</div>
      <div class="abs base-strip"></div>
    </div>

    <div class="panel panel--right">
      <h2 class="section-title" style="top:23px;color:#111">AREAS <b>COVERED</b></h2>
      <span class="section-rule" style="top:48px;background:#333"></span>

      <div class="area" style="left:75px;top:73px"><svg viewBox="0 0 12 17"><path d="M6 0a6 6 0 00-6 6c0 4.5 6 11 6 11s6-6.5 6-11a6 6 0 00-6-6z" fill="#555"/><circle cx="6" cy="6" r="2.3" fill="#f2f2f2"/></svg>SOUTHPORT</div>
      <div class="area" style="left:158px;top:73px"><svg viewBox="0 0 12 17"><path d="M6 0a6 6 0 00-6 6c0 4.5 6 11 6 11s6-6.5 6-11a6 6 0 00-6-6z" fill="#555"/><circle cx="6" cy="6" r="2.3" fill="#f2f2f2"/></svg>LIVERPOOL</div>
      <div class="area" style="left:240px;top:73px"><svg viewBox="0 0 12 17"><path d="M6 0a6 6 0 00-6 6c0 4.5 6 11 6 11s6-6.5 6-11a6 6 0 00-6-6z" fill="#555"/><circle cx="6" cy="6" r="2.3" fill="#f2f2f2"/></svg>ORMSKIRK</div>
      <div class="area" style="left:318px;top:73px"><svg viewBox="0 0 12 17"><path d="M6 0a6 6 0 00-6 6c0 4.5 6 11 6 11s6-6.5 6-11a6 6 0 00-6-6z" fill="#555"/><circle cx="6" cy="6" r="2.3" fill="#f2f2f2"/></svg>BANKS</div>

      <div class="area" style="left:75px;top:153px"><svg viewBox="0 0 12 17"><path d="M6 0a6 6 0 00-6 6c0 4.5 6 11 6 11s6-6.5 6-11a6 6 0 00-6-6z" fill="#555"/><circle cx="6" cy="6" r="2.3" fill="#f2f2f2"/></svg>HESKETH BANK</div>
      <div class="area" style="left:158px;top:153px"><svg viewBox="0 0 12 17"><path d="M6 0a6 6 0 00-6 6c0 4.5 6 11 6 11s6-6.5 6-11a6 6 0 00-6-6z" fill="#555"/><circle cx="6" cy="6" r="2.3" fill="#f2f2f2"/></svg>HALSALL</div>
      <div class="area" style="left:240px;top:153px"><svg viewBox="0 0 12 17"><path d="M6 0a6 6 0 00-6 6c0 4.5 6 11 6 11s6-6.5 6-11a6 6 0 00-6-6z" fill="#555"/><circle cx="6" cy="6" r="2.3" fill="#f2f2f2"/></svg>SCARISBRICK</div>
      <div class="area" style="left:318px;top:153px"><svg viewBox="0 0 12 17"><path d="M6 0a6 6 0 00-6 6c0 4.5 6 11 6 11s6-6.5 6-11a6 6 0 00-6-6z" fill="#555"/><circle cx="6" cy="6" r="2.3" fill="#f2f2f2"/></svg>TARLETON</div>

      <div class="area" style="left:75px;top:232px"><svg viewBox="0 0 12 17"><path d="M6 0a6 6 0 00-6 6c0 4.5 6 11 6 11s6-6.5 6-11a6 6 0 00-6-6z" fill="#555"/><circle cx="6" cy="6" r="2.3" fill="#f2f2f2"/></svg>SKELMERSDALE</div>
      <div class="area" style="left:158px;top:232px"><svg viewBox="0 0 12 17"><path d="M6 0a6 6 0 00-6 6c0 4.5 6 11 6 11s6-6.5 6-11a6 6 0 00-6-6z" fill="#555"/><circle cx="6" cy="6" r="2.3" fill="#f2f2f2"/></svg>BURSCOUGH</div>
      <div class="area" style="left:240px;top:232px"><svg viewBox="0 0 12 17"><path d="M6 0a6 6 0 00-6 6c0 4.5 6 11 6 11s6-6.5 6-11a6 6 0 00-6-6z" fill="#555"/><circle cx="6" cy="6" r="2.3" fill="#f2f2f2"/></svg>AUGHTON</div>
      <div class="area" style="left:318px;top:232px"><svg viewBox="0 0 12 17"><path d="M6 0a6 6 0 00-6 6c0 4.5 6 11 6 11s6-6.5 6-11a6 6 0 00-6-6z" fill="#555"/><circle cx="6" cy="6" r="2.3" fill="#f2f2f2"/></svg>FORMBY</div>

      <div class="abs strip-photo strip-photo--b" style="left:0" role="img" aria-label="Photo of a cleaner using a water fed pole on a brick house with large upper windows"></div>
      <div class="abs strip-word" style="left:0">FRIENDLY</div>

      <div class="abs brand-mark" style="left:91px;top:415px;width:70px;height:70px"></div>
      <div class="abs" style="left:175px;top:424px">
        <div class="brand-name" style="font-size:23px;line-height:25px">TK Bellows</div>
        <div class="brand-sub" style="font-size:11px;line-height:14px">Exterior Care Ltd</div>
        <div class="brand-tel" style="font-size:13px;line-height:17px">Tel: 01632 960 481</div>
      </div>

      <div class="abs band-foot band-foot--right" style="top:496px">WWW.TKBELLOWSEC.CO.UK</div>
      <div class="abs base-strip"></div>
    </div>
  </section>

</div>
</body>
</html>
```